Remote Computer Support PostCard

We need a Postcard Ad for marketing to businesses that need Remote Computer Support and Security. 2 sided and able to be mailed. Can be any color but color we use mostly is red. Remote Computer Support and Security per PC. Includes Remote Monitoring and Maintenance(RMM) Agent, Business Security Tools including Antivirus, Anti Malware, Ransomware Protection, Intrusion Prevention, Content Filtering and others. All remote support you need for $69.99 per pc per month.

Target Market(s)

All Businesses

Industry/Entity Type

Computer Support for Businesses

Colors
EB3D1F
EC4F4E
F09395
F8D3D4
FCEDEE

Requirements
Must have
• Bytharo, Inc. (555) 314-2968 . Sales@bytharo-example.com. Designed to be mailed. 6x9 Postcard Mailer Size Final 6.25" x 9" Ink & Bleed Four Color Process, Full Bleed Two Sides. Must have places for postage.
Nice to have
• Main lines should be in top 1/3 of postcard to stand out in mail.

```html
<!DOCTYPE html>
<html lang="en">
<head>
<meta charset="utf-8">
<title>Bytharo Remote Support Postcard</title>
<link href="https://fonts.googleapis.com/css2?family=Anton&family=Bowlby+One&family=Audiowide&family=Open+Sans:ital,wght@0,400;0,700;1,400&display=swap" rel="stylesheet">
<style>
:root{
  --stage:#4b4142;
  --red:#ef0f24;
  --red-deep:#a50f1a;
  --red-dark:#8c0a14;
  --black:#050505;
  --white:#ffffff;
  --lime:#b3ff00;
  --tick:#ffe100;
  --photo-a:#c9a27a;
  --photo-b:#e9e4dc;
}
*{margin:0;padding:0;box-sizing:border-box}
html,body{width:1200px;height:1200px;overflow:hidden;background:var(--stage)}
.canvas{position:relative;width:1200px;height:1200px}

.card{position:absolute;width:755px;height:524px;overflow:hidden}
.card--front{left:138px;top:52px;background:var(--red)}
.card--back{left:313px;top:600px;background:linear-gradient(100deg,#d80d1f 0%,#b50d1a 45%,var(--red-dark) 100%)}

.shape{position:absolute;left:0;top:0}

.headline{position:absolute;left:23px;top:26px;font-family:"Bowlby One",sans-serif;font-size:30.5px;line-height:38px;color:var(--black);-webkit-text-stroke:1px var(--white);letter-spacing:.3px;white-space:nowrap}
.offer{position:absolute;left:23px;top:104px;width:330px;height:130px;font-family:"Anton",sans-serif;color:var(--black);-webkit-text-stroke:1.5px var(--white)}
.offer__lead{position:absolute;left:0;top:24px;font-size:44px;line-height:1;letter-spacing:-1px;white-space:nowrap}
.offer__price{position:absolute;left:137px;top:0;font-size:80px;line-height:1;color:var(--lime);-webkit-text-stroke:2px var(--black);text-shadow:3px 3px 0 var(--black);letter-spacing:-1px;white-space:nowrap}
.offer__unit{position:absolute;left:50px;top:80px;font-size:50px;line-height:1;white-space:nowrap;letter-spacing:-1.5px}
.subline{position:absolute;left:24px;top:248px;width:412px;text-align:center;font-family:"Anton",sans-serif;font-size:22px;line-height:27px;color:var(--black);-webkit-text-stroke:.8px var(--white);letter-spacing:-.3px;white-space:nowrap}
.features{position:absolute;left:18px;top:309px;list-style:none;font-family:"Audiowide",sans-serif;color:var(--white);font-size:13.5px;line-height:17px;white-space:nowrap}
.features li{position:relative;padding-left:28px}
.features svg{position:absolute;left:0;top:0}
.features__note{position:absolute;left:46px;top:394px;font-family:"Audiowide",sans-serif;color:var(--white);font-size:13.5px;line-height:17px;letter-spacing:.4px;white-space:nowrap}

.brand-front{position:absolute;left:548px;top:432px;width:190px;text-align:center;color:var(--white);font-family:"Audiowide",sans-serif}
.brand-front__name{display:flex;align-items:center;justify-content:center;gap:8px;font-size:26px}
.brand-front__mark{width:14px;height:14px;background:var(--red)}
.brand-front__tag{font-family:"Open Sans",sans-serif;font-style:italic;font-size:10px;margin-top:4px}
.brand-front__phone{font-family:"Open Sans",sans-serif;font-size:7.5px;margin-top:4px}

.tab{position:absolute;left:0;top:0;width:175px;height:36px;background:var(--black);clip-path:polygon(0 0,100% 0,80% 100%,0 100%)}
.tab__label{position:absolute;left:39px;top:9px;font-family:"Bowlby One",sans-serif;font-size:16px;color:var(--white);letter-spacing:.5px}
.col{position:absolute;list-style:none;color:var(--white);font-family:"Audiowide",sans-serif}
.col--left{left:40px;top:48px;width:305px}
.col--right{left:353px;top:24px;width:370px}
.item{position:relative;padding-left:13px;margin-bottom:7px}
.col--left .item{margin-bottom:10px}
.item::before{content:"";position:absolute;left:0;top:3px;width:6px;height:6px;background:var(--tick)}
.item__title{font-size:9.2px;line-height:11px}
.item__text{font-size:6.8px;line-height:8.5px}

.back-footer{position:absolute;left:0;top:411px;width:755px;height:113px;background:var(--white)}
.brand-back{position:absolute;left:115px;top:34px;display:flex;align-items:center;gap:12px;font-family:"Audiowide",sans-serif;font-size:44px;color:#1c1c1c}
.brand-back__mark{width:20px;height:20px;background:var(--red)}
.contact{position:absolute;left:384px;top:33px;width:290px;text-align:center;font-family:"Audiowide",sans-serif;color:var(--black)}
.contact__line{font-size:17px;line-height:24px;white-space:nowrap}
.contact__mail{font-size:12.5px;line-height:22px;white-space:nowrap}
</style>
</head>
<body>
<main class="canvas">

  <section class="card card--front">
    <svg class="shape" width="755" height="524" viewBox="0 0 755 524">
      <defs>
        <linearGradient id="glow" x1="0" y1="0" x2="0" y2="1">
          <stop offset="0" stop-color="#ffffff" stop-opacity="0"/>
          <stop offset="1" stop-color="#ffffff" stop-opacity=".45"/>
        </linearGradient>
      </defs>
      <polygon points="470,0 345,184 700,320 727,308 755,308 755,0" fill="var(--red-deep)"/>
      <foreignObject x="0" y="0" width="755" height="524">
        <div role="img" aria-label="Photo of a man with coffee working at a laptop in a bright office" style="width:755px;height:308px;clip-path:polygon(483px 0,358px 184px,532px 308px,755px 308px,755px 0);background:linear-gradient(115deg,var(--photo-a) 0%,#d8c3a8 45%,var(--photo-b) 100%)"></div>
      </foreignObject>
      <rect x="0" y="474" width="520" height="15" fill="url(#glow)"/>
      <rect x="0" y="489" width="755" height="35" fill="var(--black)"/>
      <polygon points="497,489 576,411 755,411 755,489" fill="var(--black)"/>
    </svg>

    <h1 class="headline">FINALY COMPUTER SECURITY<br>AND SUPPORT MADE EASY!</h1>

    <div class="offer">
      <span class="offer__lead">FOR ONLY</span>
      <span class="offer__price">$69.99</span>
      <span class="offer__unit">PER MONTH PER PC</span>
    </div>

    <p class="subline">YOU CAN GET WORLD CLASS SECURITY SERVICES AND<br>UNLIMITED REMOTE TECHNICAL SUPPORT.</p>

    <ul class="features">
      <li><svg width="22" height="15" viewBox="0 0 22 15"><path d="M1 7 L8 13 L21 1" fill="none" stroke="var(--tick)" stroke-width="3"/></svg>AUTOMATED SYSTEM UPDATES</li>
      <li><svg width="22" height="15" viewBox="0 0 22 15"><path d="M1 7 L8 13 L21 1" fill="none" stroke="var(--tick)" stroke-width="3"/></svg>AUTOMATED SYSTEM CLEANUP</li>
      <li><svg width="22" height="15" viewBox="0 0 22 15"><path d="M1 7 L8 13 L21 1" fill="none" stroke="var(--tick)" stroke-width="3"/></svg>MANAGED ANTIVIRUS INCLUDING RANSOMWARE DETECTION AND PROTECTION</li>
      <li><svg width="22" height="15" viewBox="0 0 22 15"><path d="M1 7 L8 13 L21 1" fill="none" stroke="var(--tick)" stroke-width="3"/></svg>MONTHLY REPORTS</li>
      <li><svg width="22" height="15" viewBox="0 0 22 15"><path d="M1 7 L8 13 L21 1" fill="none" stroke="var(--tick)" stroke-width="3"/></svg>AUTOMATED REMOTE SUPPORT</li>
    </ul>
    <p class="features__note">Remote monitoring and maintenance tools monitor your<br>devices in real-time. Instantly informing you of current<br>issues and flagging potential problems.</p>

    <div class="brand-front">
      <div class="brand-front__name">Bytharo<span class="brand-front__mark"></span></div>
      <div class="brand-front__tag">Support That Just Works</div>
      <div class="brand-front__phone">555-314-2968</div>
    </div>
  </section>

  <section class="card card--back">
    <div class="tab"></div>
    <div class="tab__label">includes</div>

    <ul class="col col--left">
      <li class="item"><div class="item__title">ANTIVIRUS<br>Smart Scan</div><div class="item__text">Smart Scan leverages anti-malware and<br>antispyware signatures stored in-the-cloud.</div></li>
      <li class="item"><div class="item__title">Real-Time Scan</div><div class="item__text">Scan a file for security risks when the file is<br>received, opened, downloaded, copied, or modified.</div></li>
      <li class="item"><div class="item__title">Scheduled Scan</div><div class="item__text">Scan at the configured time and frequency. Use Scheduled Scan<br>to automate routine scans on endpoints and improve the efficiency<br>of threat management.</div></li>
      <li class="item"><div class="item__title">Manual Scan</div><div class="item__text">An on-demand scan started from the Security Agents<br>screen or the Security Agent console.</div></li>
      <li class="item"><div class="item__title">Behavior Monitoring</div><div class="item__text">Behavior Monitoring protects endpoints from unauthorized<br>changes to the operating system, registry entries, other<br>software, or files and folders.</div></li>
      <li class="item"><div class="item__title">Malware Behavior Blocking</div><div class="item__text">Block known and potential threats</div></li>
      <li class="item"><div class="item__title">Ransomware Protection</div><div class="item__text">Protect documents against unauthorized encryption or<br>modification. Automatically back up and restore files changed by<br>suspicious programs. Block processes commonly associated with<br>ransomware. Enable program inspection to detect and block<br>compromised executable files</div></li>
      <li class="item"><div class="item__title">Anti-Exploit Protection</div><div class="item__text">Terminate programs that exhibit abnormal behavior<br>associated with exploit attacks</div></li>
    </ul>

    <ul class="col col--right">
      <li class="item"><div class="item__title">Ledgerly Books Protection</div><div class="item__text">Prevent unauthorized changes to Ledgerly Books files and folders</div></li>
      <li class="item"><div class="item__title">Event Monitoring</div><div class="item__text">Monitor system events to filter potentially malicious actions</div></li>
      <li class="item"><div class="item__title">Predictive Machine Learning</div><div class="item__text">Vextral Predictive Machine Learning uses advanced machine<br>learning technology to detect emerging unknown security risks found in<br>low-prevalence suspicious processes or files.</div></li>
      <li class="item"><div class="item__title">Vulnerability Protection</div><div class="item__text">Calmguard Services now provides Intrusion Prevention Rules to protect your endpoints. Vulnerability Protection uses a host-based intrusion prevention system (HIPS) to apply virtual patches to known vulnerabilities. This feature is part of the comprehensive protection that includes Behavior Monitoring, Firewall, and Predictive Machine Learning.</div></li>
      <li class="item"><div class="item__title">Web Reputation</div><div class="item__text">Web Reputation enhances protection against malicious websites.</div></li>
      <li class="item"><div class="item__title">Browser Exploit Prevention</div><div class="item__text">Block websites containing malicious script</div></li>
      <li class="item"><div class="item__title">Firewall</div><div class="item__text">The firewall can block or allow certain types of network traffic by creating<br>a barrier between the endpoint and the network.</div></li>
      <li class="item"><div class="item__title">Device Control</div><div class="item__text">Device Control regulates access to peripheral devices.</div></li>
      <li class="item"><div class="item__title">Data Loss Prevention</div><div class="item__text">Data Loss Prevention monitors or blocks sensitive data transmissions across<br>your network.</div></li>
      <li class="item"><div class="item__title">URL Filtering</div><div class="item__text">URL Filtering allows administrators to block specific types of websites<br>during different times of the day.</div></li>
      <li class="item"><div class="item__title">Application Control</div><div class="item__text">Lets you restrict the applications that can execute or install on the endpoints.</div></li>
    </ul>

    <div class="back-footer">
      <div class="brand-back">Bytharo<span class="brand-back__mark"></span></div>
      <div class="contact">
        <div class="contact__line">Bytharo, Inc. (555) 314-2968</div>
        <div class="contact__mail">Sales@bytharo-example.com.</div>
      </div>
    </div>
  </section>

</main>
</body>
</html>
```